Business Cards that are elegant and wow

I want to create and print business cards that represent my brand and stand out from the rest. We want to ensure they stay in our branding and the integrity is not lost. I am happy to look at different shapes like square etc.

It will be printed on very thick cards and will be stylish .

I want to create and print business cards that represent my brand and stand out from the rest. We want to ensure they stay in ur branding and the integrity is not lost. I am happy to look at different shapes like square etc.

Target Market(s)

real estate professionals

Industry/Entity Type

Real Estate

Contact Information for Business Card

Maren Holt
hello@brightfernrealty.com.au
brightfernrealty.com.au
0487 316 252 (SMS)

Colors

Designer to choose colors to be used in the design.

Requirements
Must have
• My logo
• email
• website
• Name
Nice to have
• I like the idea of printing with foil or spot gloss. You want it to stand out in a sea.
Should not have
• I would like you to stay in my colour themes. Don't change the colour of my logo

```html
<!DOCTYPE html>
<html lang="en">
<head>
<meta charset="utf-8">
<title>Bright Fern Realty — Business Cards</title>
<link rel="stylesheet" href="https://fonts.googleapis.com/css2?family=Ubuntu:wght@400;500;700&display=swap">
<style>
  :root {
    --backdrop: #ece8e2;
    --card: #2a2a2c;
    --card-edge: #1d1d1f;
    --brand-blue: #3aa6dc;
    --brand-pink: #e6367f;
  }
  * { box-sizing: border-box; margin: 0; padding: 0; }
  html, body {
    width: 1200px;
    height: 1200px;
    overflow: hidden;
    background: var(--backdrop);
    font-family: "Ubuntu", sans-serif;
  }
  .sheet {
    width: 1200px;
    height: 1200px;
    display: flex;
    flex-direction: column;
    align-items: center;
    justify-content: center;
    gap: 60px;
  }
  .card {
    width: 860px;
    height: 491px;
    background: var(--card);
    border-radius: 4px;
    box-shadow: 0 10px 24px rgba(0,0,0,0.18), 0 0 0 1px var(--card-edge);
    display: flex;
    align-items: center;
    justify-content: center;
  }
  .brand {
    display: flex;
    align-items: center;
    gap: 22px;
  }
  .brand-dot {
    width: 78px;
    height: 78px;
    border-radius: 50%;
    border: 5px solid var(--brand-blue);
    flex: none;
  }
  .brand-name {
    font-weight: 500;
    color: var(--brand-blue);
    font-size: 54px;
    letter-spacing: 1px;
    text-transform: uppercase;
    line-height: 1;
  }
  .card--front .brand-dot { width: 64px; height: 64px; border-width: 4px; }
  .card--front .brand-name { font-size: 32px; }
  .card--front .front-row {
    display: flex;
    align-items: center;
    gap: 26px;
  }
  .divider {
    width: 3px;
    height: 110px;
    background: var(--brand-pink);
  }
  .contact { color: var(--brand-blue); }
  .contact-name {
    font-weight: 700;
    font-size: 32px;
    margin-bottom: 10px;
  }
  .contact-list { list-style: none; }
  .contact-list li {
    display: flex;
    align-items: center;
    gap: 12px;
    font-size: 19px;
    line-height: 1.45;
  }
  .contact-list svg {
    width: 16px;
    height: 16px;
    flex: none;
    fill: none;
    stroke: var(--brand-pink);
    stroke-width: 2;
  }
</style>
</head>
<body>
<main class="sheet">
  <section class="card card--back">
    <div class="brand">
      <span class="brand-dot"></span>
      <span class="brand-name">Bright Fern Realty</span>
    </div>
  </section>

  <section class="card card--front">
    <div class="front-row">
      <div class="brand">
        <span class="brand-dot"></span>
        <span class="brand-name">Bright Fern Realty</span>
      </div>
      <span class="divider"></span>
      <div class="contact">
        <p class="contact-name">Maren Holt</p>
        <ul class="contact-list">
          <li>
            <svg viewBox="0 0 16 16" aria-hidden="true"><path d="M4 1.5l2.5 3-1.5 2c1 2 2.5 3.5 4.5 4.5l2-1.5 3 2.5-1.5 2.5C7 14 2 9 1.5 3z"/></svg>
            +0487 316 252 (SMS)
          </li>
          <li>
            <svg viewBox="0 0 16 16" aria-hidden="true"><rect x="1.5" y="3.5" width="13" height="9"/><path d="M1.5 3.5l6.5 5 6.5-5"/></svg>
            hello@brightfernrealty.com.au
          </li>
          <li>
            <svg viewBox="0 0 16 16" aria-hidden="true"><circle cx="8" cy="8" r="6.5"/><ellipse cx="8" cy="8" rx="3" ry="6.5"/><path d="M1.5 8h13"/></svg>
            brightfernrealty.com.au
          </li>
        </ul>
      </div>
    </div>
  </section>
</main>
</body>
</html>
```